Design a helpdesk ticketing platform *

We are launching a helpdesk ticketing platform. Very much like quellbox.com, merrylark.com, pivolta.com, brisktray.com etc. We have a full mid-fidelity prototype built and we want someone to build the full fidelity of the product.

You can view the full mid-fidelity prototype here: https://lnk.vexora.net/Qa8Lpw

The best way moving forward is to just design the following 4 pages

- Main Dashboard https://lnk.vexora.net/81hRtd
- All tickets https://lnk.vexora.net/jwNoEb
- Viewing a ticket https://lnk.vexora.net/Ys4VmK
- Contacts https://lnk.vexora.net/pHeXuo

Target Market(s)

Small business owners

Industry/Entity Type

Saas

Number of Pages Required

4 page

Font styles to use
Serif
Sans Serif

Colors

Designer to choose colors to be used in the design.

Requirements
Must have
• Must follow the prototype exactly. We are not looking for any UX changes. We want the designe xactly as the prototype is. We are only looking for design ideas.
Should not have
• modern, clean. We'd love to see the primary color as yellow, purple, orange, green or blue. You choose which one you think looks best and go with that.

```html
<!DOCTYPE html>
<html lang="en">
<head>
<meta charset="utf-8">
<title>deskharbor — Dashboard</title>
<link rel="stylesheet" href="https://fonts.googleapis.com/css2?family=Roboto:wght@400;500;700&family=Roboto+Condensed:wght@400;700&display=swap">
<style>
  :root {
    --page-bg: #6c7c9c;
    --brand: #1ea1f2;
    --side: #3e4859;
    --side-dark: #323b4a;
    --side-active: #4a5568;
    --side-text: #c9d0da;
    --main-bg: #eef1f5;
    --white: #ffffff;
    --ink: #333a44;
    --muted: #8a929c;
    --line: #e3e7ec;
    --link: #2a9ad8;
    --yellow: #f7b21d;
    --blue: #1f8dd0;
    --green: #8ccb7b;
    --teal: #20c3cd;
    --red: #e0413a;
    --ok: #17a449;
  }
  * { box-sizing: border-box; margin: 0; padding: 0; }
  html, body { width: 857px; height: 1200px; overflow: hidden; }
  body { background: var(--page-bg); font-family: "Roboto", sans-serif; color: var(--ink); position: relative; }

  .app {
    position: absolute; left: 0; top: 355px;
    width: 935px; height: 534px;
    transform: scale(0.9166); transform-origin: top left;
    display: flex; background: var(--main-bg); overflow: hidden;
  }

  /* Sidebar */
  .sidebar { width: 148px; background: var(--side); flex: none; }
  .brand { height: 54px; background: var(--brand); color: var(--white); font-weight: 700; font-size: 17px; letter-spacing: .5px; display: flex; align-items: center; padding-left: 22px; }
  .new-ticket { height: 42px; background: var(--side-dark); color: var(--side-text); font-size: 9.5px; display: flex; align-items: center; padding-left: 18px; letter-spacing: .3px; }
  .nav { list-style: none; }
  .nav-item { height: 35px; display: flex; align-items: center; padding-left: 18px; color: var(--side-text); font-size: 7.5px; font-weight: 700; letter-spacing: .4px; position: relative; }
  .nav-item svg { width: 13px; height: 13px; margin-right: 8px; stroke: var(--side-text); fill: none; stroke-width: 1.3; }
  .nav-item.is-active { background: var(--side-active); color: var(--white); border-left: 3px solid var(--brand); padding-left: 15px; font-size: 6.5px; }
  .nav-item .chevron { position: absolute; right: 12px; width: 11px; height: 11px; margin: 0; }

  /* Main */
  .main { flex: 1; position: relative; }
  .topbar { height: 54px; background: var(--white); display: flex; align-items: center; border-bottom: 1px solid var(--line); }
  .menu-toggle { width: 67px; height: 100%; display: flex; align-items: center; justify-content: center; border-right: 1px solid var(--line); }
  .search { display: flex; align-items: center; padding-left: 16px; color: #9aa2ab; font-size: 11px; flex: 1; }
  .search svg { margin-right: 15px; }
  .user { display: flex; align-items: center; padding-right: 18px; font-size: 10px; color: #555c66; }
  .avatar { width: 32px; height: 32px; border-radius: 50%; margin: 0 10px; background: radial-gradient(circle at 50% 45%, #d9a98a, #9a6a4f 70%, #c9c9c9 72%); }
  .kebab { display: flex; flex-direction: column; gap: 2px; }
  .kebab span { width: 4px; height: 4px; border-radius: 50%; background: #666; }

  .page-head { padding: 20px 13px 0; display: flex; align-items: baseline; gap: 7px; }
  .page-title { font-size: 14px; font-weight: 500; letter-spacing: .3px; }
  .page-sub { font-size: 10px; color: var(--muted); }

  .stats { display: flex; gap: 10px; padding: 21px 13px 0; }
  .stat { width: 145px; height: 67px; background: var(--white); display: flex; box-shadow: 0 1px 2px rgba(0,0,0,.08); }
  .stat-icon { width: 55px; display: flex; align-items: center; justify-content: center; }
  .stat-body { padding: 18px 0 0 8px; }
  .stat-label { font-family: "Roboto Condensed", sans-serif; font-size: 11px; font-weight: 700; }
  .stat-value { font-size: 23px; font-weight: 500; color: var(--ink); line-height: 1.2; padding-left: 2px; }
  .stat--yellow .stat-icon { background: var(--yellow); } .stat--yellow .stat-label { color: var(--yellow); }
  .stat--blue .stat-icon { background: var(--blue); } .stat--blue .stat-label { color: var(--blue); }
  .stat--green .stat-icon { background: var(--green); } .stat--green .stat-label { color: var(--green); }
  .stat--teal .stat-icon { background: var(--teal); } .stat--teal .stat-label { color: var(--teal); }
  .stat--red .stat-icon { background: var(--red); } .stat--red .stat-label { color: var(--red); }

  .activity { position: absolute; left: 13px; right: 13px; top: 208px; bottom: 0; background: var(--white); border-top: 2px solid #dde2e8; }
  .activity-title { font-size: 16px; font-weight: 400; padding: 13px 8px 0; color: #2f353d; }
  .activity-table { border-collapse: collapse; margin: 27px 8px 0; width: 743px; font-size: 10px; }
  .activity-table th { text-align: left; font-weight: 700; font-size: 11px; height: 32px; border-bottom: 1px solid var(--line); }
  .activity-table td { height: 32.5px; border-bottom: 1px solid var(--line); color: var(--ink); }
  .activity-table th, .activity-table td { padding-left: 7px; }
  .col-num { width: 21px; }
  .col-title { width: 358px; border-right: 1px solid var(--line); }
  .col-updated { width: 308px; border-right: 1px solid var(--line); font-size: 11px; }
  .title-link { color: var(--link); font-size: 9.5px; }
  .badge { display: inline-block; padding: 2px 5px; border-radius: 4px; color: var(--white); font-size: 9px; font-weight: 700; }
  .badge--open { background: var(--ok); }
  .badge--closed { background: var(--red); }
</style>
</head>
<body>
<div class="app">
  <aside class="sidebar">
    <div class="brand">deskharbor</div>
    <div class="new-ticket">NEW TICKET</div>
    <ul class="nav">
      <li class="nav-item is-active"><svg viewBox="0 0 14 14"><circle cx="7" cy="7" r="5.5"/><path d="M7 7l2.5-2"/></svg>DASHBOARD</li>
      <li class="nav-item"><svg viewBox="0 0 14 14"><rect x="2" y="3" width="8" height="10"/><path d="M4 1h8v10"/></svg>TICKETS<svg class="chevron" viewBox="0 0 12 12"><path d="M1 4l5 5 5-5"/></svg></li>
      <li class="nav-item"><svg viewBox="0 0 14 14"><circle cx="7" cy="5" r="3"/><path d="M1.5 13c1-3 3-4 5.5-4s4.5 1 5.5 4z"/></svg>CONTACTS</li>
      <li class="nav-item"><svg viewBox="0 0 14 14"><circle cx="7" cy="7" r="2"/><circle cx="7" cy="7" r="5.5" stroke-dasharray="2 1.5"/></svg>ADMIN SETTING<svg class="chevron" viewBox="0 0 12 12"><path d="M1 4l5 5 5-5"/></svg></li>
      <li class="nav-item"><svg viewBox="0 0 14 14"><rect x="1.5" y="1.5" width="11" height="11"/><path d="M4 5h2M8 5h2M4 9h2M8 9h2"/></svg>ACCOUNT &amp; BILLING</li>
    </ul>
  </aside>

  <main class="main">
    <header class="topbar">
      <div class="menu-toggle">
        <svg width="24" height="14" viewBox="0 0 24 14"><path d="M4 3l-3 4 3 4" fill="none" stroke="#1ea1f2" stroke-width="1.5"/><path d="M7 2h16M7 7h16M7 12h16" stroke="#b7c0cb" stroke-width="2"/></svg>
      </div>
      <div class="search">
        <svg width="15" height="15" viewBox="0 0 15 15"><circle cx="6" cy="6" r="4.8" fill="none" stroke="#9aa2ab" stroke-width="1.6"/><path d="M9.5 9.5l4 4" stroke="#9aa2ab" stroke-width="1.8"/></svg>
        Search for tickets,....
      </div>
      <div class="user">
        Milo Vantrell
        <div class="avatar" role="img" aria-label="User profile photo"></div>
        <div class="kebab"><span></span><span></span><span></span></div>
      </div>
    </header>

    <div class="page-head">
      <h1 class="page-title">DASHBOARD</h1>
      <span class="page-sub">Ticket summary</span>
    </div>

    <section class="stats">
      <div class="stat stat--yellow">
        <div class="stat-icon"><svg width="36" height="32" viewBox="0 0 36 32" fill="none" stroke="#fff" stroke-width="2"><path d="M4 14l20-10 3 5a3 3 0 0 0 3 5l3 5-20 10-3-5a3 3 0 0 0-3-5z"/><path d="M12 14l8-4M14 19l8-4"/></svg></div>
        <div class="stat-body"><div class="stat-label">OPEN TICKETS</div><div class="stat-value">16</div></div>
      </div>
      <div class="stat stat--blue">
        <div class="stat-icon"><svg width="30" height="30" viewBox="0 0 30 30" fill="none" stroke="#fff" stroke-width="2"><rect x="3" y="6" width="24" height="21" rx="2"/><path d="M3 12h24M9 3v6M21 3v6M10 19l4 4 7-8"/></svg></div>
        <div class="stat-body"><div class="stat-label">DUE TODAY</div><div class="stat-value">14</div></div>
      </div>
      <div class="stat stat--green">
        <div class="stat-icon"><svg width="36" height="32" viewBox="0 0 36 32" fill="none" stroke="#fff" stroke-width="2"><path d="M4 14l20-10 3 5a3 3 0 0 0 3 5l3 5-20 10-3-5a3 3 0 0 0-3-5z"/><path d="M12 14l8-4M14 19l8-4"/></svg></div>
        <div class="stat-body"><div class="stat-label">UNASSIGNED</div><div class="stat-value">14</div></div>
      </div>
      <div class="stat stat--teal">
        <div class="stat-icon"><svg width="36" height="32" viewBox="0 0 36 32" fill="none" stroke="#fff" stroke-width="2"><path d="M4 14l20-10 3 5a3 3 0 0 0 3 5l3 5-20 10-3-5a3 3 0 0 0-3-5z"/><path d="M12 14l8-4M14 19l8-4"/></svg></div>
        <div class="stat-body"><div class="stat-label">OVER DUE</div><div class="stat-value">0</div></div>
      </div>
      <div class="stat stat--red">
        <div class="stat-icon"><svg width="30" height="30" viewBox="0 0 30 30" fill="none" stroke="#fff" stroke-width="2.6"><circle cx="15" cy="15" r="11"/><path d="M7.5 22.5l15-15"/></svg></div>
        <div class="stat-body"><div class="stat-label">NOT RESOLVED</div><div class="stat-value">11</div></div>
      </div>
    </section>

    <section class="activity">
      <h2 class="activity-title">Recent Activites</h2>
      <table class="activity-table">
        <thead>
          <tr><th class="col-num">#</th><th class="col-title">Title</th><th class="col-updated">Updated</th><th>Status</th></tr>
        </thead>
        <tbody>
          <tr><td class="col-num">1</td><td class="col-title"><span class="title-link">marcus Lenn assigned forgot to cc, trying again (#15) to marcus Lenn</span></td><td class="col-updated">2018-11-03 13:18:19</td><td><span class="badge badge--open">Opened</span></td></tr>
          <tr><td class="col-num">2</td><td class="col-title"><span class="title-link">marcus Lenn assigned forgot to cc, trying again (#15) to marcus Lenn</span></td><td class="col-updated">2018-11-03 11:21:56</td><td><span class="badge badge--open">Opened</span></td></tr>
          <tr><td class="col-num">3</td><td class="col-title"><span class="title-link">marcus Lenn assigned forgot to cc, trying again (#15) to marcus Lenn</span></td><td class="col-updated">2018-11-03 11:03:28</td><td><span class="badge badge--open">Opened</span></td></tr>
          <tr><td class="col-num">4</td><td class="col-title"><span class="title-link">marcus Lenn assigned forgot to cc, trying again (#15) to marcus Lenn</span></td><td class="col-updated">2018-11-03 09:05:55</td><td><span class="badge badge--closed">Closed</span></td></tr>
          <tr><td class="col-num">5</td><td class="col-title"><span class="title-link">marcus Lenn assigned forgot to cc, trying again (#15) to marcus Lenn</span></td><td class="col-updated">2018-09-16 12:37:04</td><td><span class="badge badge--closed">Closed</span></td></tr>
        </tbody>
      </table>
    </section>
  </main>
</div>
</body>
</html>
```